Business Card for Freelance Copywriting & Web Design Business

Hi! I have a logo but want a new business card. Here's a better idea of what I'm thinking:
-Brand new double-sided business card, rounded cards, embossed logo, nice quality paper
-Include phone (604-382-5194), email (hello@lauraberndt.org), and website (www.lauraberndt.org). No address, please, since I service clients worldwide.
-I'd like the fonts to match those on my website (www.lauraberndt.org). I had to purchase the one font (Born Ready), attached. I'm not sure which version was used on my site so I included all that I purchased. The secondary font is Helvetica
-I'd also like the tagline "Powerful Words. Impressive Results." included.
-My primary brand colour is the teal, colour #19ADC3
Laura Berndt | Laura Berndt Copywriting & Web Design <hello@lauraberndt.org>
-I'd also like the following services listed on the new cards:
SEO Website Content
SEO Blog Content
SEO Website Design
Contact Information for Business Card
as stated in brief
Font styles to use
Other font styles liked:
- See brief
Look and feel
Each slider illustrates characteristics of the customer's brand and the style your logo design should communicate.

```html
<!DOCTYPE html>
<html lang="en">
<head>
<meta charset="utf-8">
<title>Laura Berndt — Business Card</title>
<link rel="stylesheet" href="https://fonts.googleapis.com/css2?family=Arimo:wght@400&family=Allura&display=swap">
<style>
  :root {
    --backdrop: #2e2e2e;
    --card: #1b1b1b;
    --card-edge: #262626;
    --emboss: #3a3a3a;
    --emboss-dim: #333333;
    --ink: #f2f2f2;
    --teal: #19adc3;
  }
  * { margin: 0; padding: 0; box-sizing: border-box; }
  html, body { width: 1200px; height: 689px; overflow: hidden; background: var(--backdrop); }
  .canvas {
    position: relative; width: 1200px; height: 689px;
    display: flex; align-items: center; justify-content: center; gap: 48px;
    font-family: "Arimo", Helvetica, Arial, sans-serif;
  }
  .card {
    position: relative; width: 520px; height: 300px;
    background: var(--card); border-radius: 26px;
    border: 1px solid var(--card-edge);
    box-shadow: 0 18px 40px rgba(0,0,0,.45);
    overflow: hidden;
  }
  .brand-mark {
    position: absolute; display: flex; align-items: center; gap: 12px;
    color: var(--emboss); font-size: 34px; letter-spacing: 1px;
  }
  .brand-mark .dot {
    width: 30px; height: 30px; border-radius: 50%; background: var(--emboss-dim);
  }
  .brand-sub {
    position: absolute; color: var(--emboss); font-size: 11px;
    letter-spacing: 4px; text-transform: uppercase;
  }
  .card--front .brand-mark { left: 120px; top: 70px; }
  .card--front .brand-sub { left: 162px; top: 116px; }
  .tagline {
    position: absolute; left: 0; right: 0; top: 190px; text-align: center;
    color: var(--ink); font-size: 25px; letter-spacing: .3px;
  }
  .card--back .brand-mark { left: 200px; top: 44px; font-size: 30px; }
  .card--back .brand-sub { left: 242px; top: 86px; font-size: 10px; }
  .contact { position: absolute; left: 40px; top: 140px; }
  .contact-name {
    font-family: "Allura", cursive; color: var(--teal);
    font-size: 46px; line-height: 1;
  }
  .contact-role { color: var(--ink); font-size: 16px; margin: 4px 0 12px 6px; }
  .contact-list { list-style: none; margin-left: 6px; }
  .contact-list li {
    display: flex; align-items: center; gap: 12px;
    color: var(--ink); font-size: 15px; line-height: 24px;
  }
  .contact-list svg { width: 16px; height: 16px; fill: var(--teal); flex: none; }
</style>
</head>
<body>
<main class="canvas">
  <section class="card card--front" aria-label="Card front">
    <div class="brand-mark"><span class="dot"></span><span>Laura Berndt</span></div>
    <div class="brand-sub">Copywriting &amp; Web Design</div>
    <p class="tagline">Powerful Words. Impressive Results</p>
  </section>

  <section class="card card--back" aria-label="Card back">
    <div class="brand-mark"><span class="dot"></span><span>Laura Berndt</span></div>
    <div class="brand-sub">Copywriting &amp; Web Design</div>
    <div class="contact">
      <p class="contact-name">Laura Berndt</p>
      <p class="contact-role">Copywriting &amp; Web Design</p>
      <ul class="contact-list">
        <li>
          <svg viewBox="0 0 24 24" aria-hidden="true"><path d="M6.6 10.8a15.1 15.1 0 0 0 6.6 6.6l2.2-2.2a1 1 0 0 1 1-.25 11.4 11.4 0 0 0 3.6.57 1 1 0 0 1 1 1V20a1 1 0 0 1-1 1A17 17 0 0 1 3 4a1 1 0 0 1 1-1h3.5a1 1 0 0 1 1 1c0 1.25.2 2.45.57 3.6a1 1 0 0 1-.25 1z"/></svg>
          (604-382-5194)
        </li>
        <li>
          <svg viewBox="0 0 24 24" aria-hidden="true"><path d="M2 5h20v14H2z M2 5l10 8 10-8" fill="var(--teal)"/><path d="M3 6l9 7 9-7" fill="none" stroke="#1b1b1b" stroke-width="1.6"/></svg>
          hello@lauraberndt.org
        </li>
        <li>
          <svg viewBox="0 0 24 24" aria-hidden="true"><circle cx="12" cy="12" r="10"/><path d="M2 12h20M12 2c3 3 3 17 0 20M12 2c-3 3-3 17 0 20" fill="none" stroke="#1b1b1b" stroke-width="1.4"/></svg>
          www.lauraberndt.org
        </li>
      </ul>
    </div>
  </section>
</main>
</body>
</html>
```